Tidewake Charter Angling Tradeshow Booth

Im looking for a professional and attractive, eye catching trade show booth design

Target Market(s)

professionals who are looking to go on a high end fishing excursion

Industry/Entity Type

sport fishing

Requirements
Must have
• my website (www.tidewakecharterangling,com) my logo,

```html
<!DOCTYPE html>
<html lang="en">
<head>
<meta charset="utf-8">
<title>Tidewake Charter Angling – Tradeshow Booth</title>
<link href="https://fonts.googleapis.com/css2?family=Great+Vibes&family=Oswald:wght@500;700&family=Poppins:wght@300;500;600;700&display=swap" rel="stylesheet">
<style>
  :root{
    --page:#a3a3a3;
    --navy:#0f2f5c;
    --ink:#1f1f1f;
    --sea-deep:#17366d;
    --sea-mid:#2a5596;
    --sky-top:#f4f7fb;
    --sky-mid:#e6ebf0;
    --sunset:#f2b66a;
    --sunset-deep:#e8944a;
    --gold:#f5c62f;
    --white:#ffffff;
    --deck:#c9b8a6;
  }
  *{margin:0;padding:0;box-sizing:border-box}
  html,body{width:926px;height:1200px;overflow:hidden;background:var(--page)}
  .booth{
    position:absolute;left:23px;top:160px;width:880px;height:880px;
    background:var(--white);overflow:hidden;
    font-family:"Poppins",sans-serif;
  }
  .sky{
    position:absolute;left:0;top:0;width:880px;height:420px;
    background:linear-gradient(180deg,var(--sky-top) 0%,var(--sky-mid) 45%,#f0d6ae 72%,var(--sunset) 86%,var(--sunset-deep) 100%);
  }
  .sun{
    position:absolute;left:125px;top:370px;width:40px;height:16px;border-radius:50%;
    background:radial-gradient(ellipse,#fffbe0 0%,#ffe07a 50%,rgba(255,200,90,0) 100%);
  }
  .sea{position:absolute;left:0;top:355px;width:880px;height:395px}
  .angler-photo{
    position:absolute;left:555px;top:275px;width:325px;height:475px;
    background:linear-gradient(170deg,#d9c7a8 0%,#4a3a30 35%,#2c2624 60%,var(--deck) 100%);
    clip-path:polygon(18% 0,100% 8%,100% 100%,0 100%,0 62%,10% 40%);
  }
  .snapshot{
    position:absolute;border:6px solid var(--white);
    box-shadow:0 4px 10px rgba(0,0,0,.35);
  }
  .snapshot--crew{
    left:355px;top:345px;width:190px;height:135px;transform:rotate(-27deg);
    background:linear-gradient(160deg,#8aa6c3,#5d5a55 60%,#7a7468);
  }
  .snapshot--catch{
    left:380px;top:548px;width:180px;height:130px;transform:rotate(14deg);
    background:linear-gradient(170deg,#9db7d4,#3f4f66 55%,#c7cdd3);
  }
  .script-your{
    position:absolute;left:75px;top:58px;
    font-family:"Great Vibes",cursive;font-size:78px;color:var(--ink);line-height:1;
  }
  .region{
    position:absolute;left:70px;top:130px;
    font-weight:700;font-size:57px;color:var(--ink);letter-spacing:.3px;line-height:1;
  }
  .headline{
    position:absolute;left:68px;top:182px;
    font-family:"Oswald",sans-serif;font-weight:700;font-size:95px;color:var(--navy);
    line-height:1;letter-spacing:-1px;transform:scaleY(1.18);transform-origin:top left;
  }
  .tagline{
    position:absolute;left:70px;top:296px;
    font-weight:500;font-size:31px;color:var(--ink);line-height:1;
  }
  .brand{position:absolute;left:630px;top:83px;width:210px;text-align:center}
  .brand-boat{
    display:block;margin:0 auto;width:176px;height:135px;
    background:linear-gradient(180deg,rgba(210,220,230,.35),rgba(230,226,170,.8));
  }
  .brand-name{
    margin-top:22px;font-weight:700;font-size:10.5px;color:var(--ink);letter-spacing:.3px;line-height:1.1;
  }
  .brand-town{font-weight:700;font-size:5.5px;color:var(--ink);letter-spacing:.5px}
  .features{position:absolute;left:74px;top:448px;list-style:none}
  .feature{
    display:flex;align-items:center;gap:11px;height:53px;
    font-weight:700;font-size:27px;color:var(--white);
  }
  .feature svg{width:17px;height:17px;flex:none}
  .connect{
    position:absolute;left:72px;top:694px;font-size:29px;line-height:1;color:var(--white);letter-spacing:1px;
  }
  .connect strong{color:var(--gold);font-weight:700}
  .connect span{font-weight:300}
  .contact-bar{
    position:absolute;left:0;top:750px;width:880px;height:130px;background:var(--white);
  }
  .contact{
    position:absolute;left:68px;top:27px;display:flex;align-items:center;
    font-family:"Oswald",sans-serif;font-weight:500;font-size:27px;color:var(--ink);
    letter-spacing:-.6px;line-height:1;
  }
  .contact .phone-icon{width:30px;height:30px;margin-right:8px}
  .contact .divider{width:3px;height:32px;background:var(--ink);margin:0 11px}
  .social{display:flex;gap:6px;margin-left:22px}
  .social-dot{width:20px;height:20px;border-radius:4px;background:var(--navy)}
</style>
</head>
<body>
<main class="booth">
  <div class="sky"></div>
  <div class="sun"></div>

  <svg class="sea" viewBox="0 0 880 395" role="img" aria-label="Photo of open sea at sunset">
    <defs>
      <linearGradient id="seaFill" x1="0" y1="0" x2="0" y2="1">
        <stop offset="0" stop-color="#1d3f7a"/>
        <stop offset=".5" stop-color="#2a5596"/>
        <stop offset="1" stop-color="#17366d"/>
      </linearGradient>
    </defs>
    <path d="M0 40 C30 40 40 10 70 10 S110 40 140 40 S180 10 210 10 S250 40 280 40 S320 10 350 10 S390 40 420 40 S460 10 490 10 S530 40 560 40 S600 10 630 10 S670 40 700 40 S740 10 770 10 S810 40 840 40 S870 15 880 12 L880 395 L0 395 Z" fill="url(#seaFill)"/>
    <path d="M0 40 C30 40 40 10 70 10 S110 40 140 40 S180 10 210 10 S250 40 280 40 S320 10 350 10 S390 40 420 40 S460 10 490 10 S530 40 560 40 S600 10 630 10 S670 40 700 40 S740 10 770 10 S810 40 840 40 S870 15 880 12" fill="none" stroke="#ffffff" stroke-width="9" transform="translate(0 -4)"/>
    <polygon points="340,395 880,230 880,395" fill="#cdb9a4" opacity=".85"/>
  </svg>

  <div class="angler-photo" role="img" aria-label="Photo of an angler on a boat deck holding a large tuna"></div>
  <div class="snapshot snapshot--crew" role="img" aria-label="Photo of a group of anglers on a dock showing their catch"></div>
  <div class="snapshot snapshot--catch" role="img" aria-label="Photo of two anglers on a boat with a tuna"></div>

  <div class="script-your">Your</div>
  <div class="region">HUDSON VALLEY</div>
  <h1 class="headline">FISHING HUB</h1>
  <p class="tagline">Local Gear, Expert Advice!</p>

  <div class="brand">
    <span class="brand-boat" role="img" aria-label="Line drawing of a sportfishing boat"></span>
    <p class="brand-name">TIDEWAKE CHARTER ANGLING</p>
    <p class="brand-town">HARBORVIEW, N.Y</p>
  </div>

  <ul class="features">
    <li class="feature"><svg viewBox="0 0 20 20"><circle cx="10" cy="10" r="10" fill="#f5c62f"/><path d="M5.5 10.2l3 3 6-6" fill="none" stroke="#17366d" stroke-width="2.4" stroke-linecap="round" stroke-linejoin="round"/></svg>One-Stop Shop</li>
    <li class="feature"><svg viewBox="0 0 20 20"><circle cx="10" cy="10" r="10" fill="#f5c62f"/><path d="M5.5 10.2l3 3 6-6" fill="none" stroke="#17366d" stroke-width="2.4" stroke-linecap="round" stroke-linejoin="round"/></svg>Local Expertise</li>
    <li class="feature"><svg viewBox="0 0 20 20"><circle cx="10" cy="10" r="10" fill="#f5c62f"/><path d="M5.5 10.2l3 3 6-6" fill="none" stroke="#17366d" stroke-width="2.4" stroke-linecap="round" stroke-linejoin="round"/></svg>Community Focus</li>
    <li class="feature"><svg viewBox="0 0 20 20"><circle cx="10" cy="10" r="10" fill="#f5c62f"/><path d="M5.5 10.2l3 3 6-6" fill="none" stroke="#17366d" stroke-width="2.4" stroke-linecap="round" stroke-linejoin="round"/></svg>Trusted Advice</li>
  </ul>

  <p class="connect"><strong>CONNECT</strong> <span>WITH US</span></p>

  <footer class="contact-bar">
    <div class="contact">
      <svg class="phone-icon" viewBox="0 0 32 32"><circle cx="16" cy="16" r="15" fill="#0f2f5c"/><path d="M11.5 8.5c.6-.4 1.4-.3 1.8.3l1.6 2.4c.4.6.3 1.3-.2 1.8l-1 1c.8 1.8 2.2 3.3 4 4.2l1-1c.5-.5 1.2-.6 1.8-.2l2.4 1.5c.6.4.8 1.2.4 1.8l-.9 1.4c-.5.8-1.5 1.2-2.4.9-4.4-1.3-7.8-4.8-9.1-9.2-.3-.9.1-1.9.9-2.4z" fill="#ffffff"/></svg>
      <span>+1 845-555-0142</span>
      <span class="divider"></span>
      <span>WWW.TIDEWAKECHARTERANGLING.COM</span>
      <span class="social" aria-label="Social media links">
        <span class="social-dot"></span>
        <span class="social-dot"></span>
        <span class="social-dot"></span>
      </span>
    </div>
  </footer>
</main>
</body>
</html>
```